Antigen Preservation Bureau

The company will provide a contract research services to stabilize various viruses, viral vectors, and vaccines. It may offer some licensing opportunities for stabilizing technologies. Main area of applications are pharmaceutical, therapeutic, and vaccination field. The company aspires to develop room temperature vaccines for global distribution beyond the current cold chain.

Target Market(s)

pharmaceutical, therapeutic and vaccination fields

Coding

Coded - Design and coding required

Number of Pages Required

4 page

Requirements
Must have
• Incorporate a APB logo, attached at the bottom, on the Web page

```html
<!DOCTYPE html>
<html lang="en">
<head>
<meta charset="utf-8">
<title>Antigen Preservation Bureau</title>
<link rel="stylesheet" href="https://fonts.googleapis.com/css2?family=Mulish:wght@400;600;700&family=Questrial&display=swap">
<style>
:root{
  --gold:#c99f4f;
  --gold-text:#c8963c;
  --green:#3f9b80;
  --green-dark:#2f7f68;
  --ink:#4a4a4a;
  --muted:#6d6d6d;
  --gray-band:#f3f3f3;
  --footer:#3b3b3b;
  --footer-line:#555;
  --white:#ffffff;
  --hero-deep:#06142f;
  --hero-mid:#1c4a8c;
}
*{box-sizing:border-box;margin:0;padding:0}
html,body{width:1200px;height:2736px;overflow:hidden}
body{position:relative;background:var(--white);font-family:"Questrial",sans-serif;color:var(--ink)}
.abs{position:absolute}

/* header */
.site-header{position:absolute;left:0;top:0;width:1200px;height:80px;background:var(--white)}
.brand{position:absolute;left:142px;top:16px;display:flex;align-items:center;gap:12px}
.brand-square{width:44px;height:44px;border:3px solid var(--green)}
.brand-name{font-family:"Questrial",sans-serif;color:var(--green);font-size:14px;line-height:16px;letter-spacing:1.5px;text-transform:uppercase;width:150px}
.header-phone{position:absolute;left:940px;top:10px;display:flex;align-items:center;gap:12px;font-size:14px;color:var(--ink)}
.phone-dot{width:24px;height:24px;border-radius:50%;background:var(--gold);display:flex;align-items:center;justify-content:center}
.main-nav{position:absolute;right:144px;top:50px;display:flex;gap:50px;font-size:13px;letter-spacing:.5px;text-transform:uppercase}
.main-nav a{color:var(--ink);text-decoration:none;padding-bottom:4px}
.main-nav a.active{color:var(--green);border-bottom:2px solid var(--green)}

/* hero */
.hero{position:absolute;left:0;top:80px;width:1200px;height:460px;
  background:radial-gradient(circle at 22% 42%,#3c6fb8 0,#1a3f7c 22%,transparent 42%),
             radial-gradient(circle at 78% 40%,#3a6ab0 0,#183a74 20%,transparent 40%),
             linear-gradient(180deg,var(--hero-mid),var(--hero-deep))}
.hero-title{position:absolute;left:0;top:210px;width:1200px;text-align:center;color:var(--white);font-size:30px;line-height:40px;letter-spacing:.5px}
.hero-dots{position:absolute;left:560px;top:462px;display:flex;gap:8px}
.hero-dots span{width:20px;height:20px;border-radius:50%;border:2px solid #cfd8e6;background:transparent}
.hero-dots span.on{background:var(--gold)}

/* what we do */
.services-band{position:absolute;left:0;top:540px;width:1200px;height:281px;background:var(--gold)}
.section-title{font-family:"Mulish",sans-serif;font-weight:700;text-align:center;font-size:31px}
.services-title{position:absolute;left:0;top:594px;width:1200px;color:var(--white)}
.title-rule{position:absolute;height:2px;width:70px}
.services-rule{left:565px;top:643px;background:var(--white)}
.services-intro{position:absolute;left:0;top:670px;width:1200px;text-align:center;color:var(--white);font-family:"Mulish",sans-serif;font-size:12.5px;line-height:22px}
.card{position:absolute;top:742px;width:288px;height:334px;background:var(--white);border:1px solid #e2e2e2;text-align:center}
.card-icon{position:absolute;left:107px;top:50px;width:74px;height:74px;border-radius:50%;border:4px solid var(--green)}
.card-title{position:absolute;left:0;top:162px;width:100%;font-size:15px;letter-spacing:.8px;color:#6d8a85;text-transform:uppercase}
.card-text{position:absolute;left:40px;top:194px;width:208px;font-family:"Mulish",sans-serif;font-size:11.5px;line-height:22px;color:var(--ink)}
.card-link{position:absolute;left:0;top:278px;width:100%;font-family:"Mulish",sans-serif;font-size:13px;color:var(--green);display:flex;justify-content:center;align-items:center;gap:16px}
.card--featured{background:linear-gradient(160deg,#4a3a38,#2c2626 55%,#7a5a4c);border:4px solid #d6d6d6}
.card--featured .card-icon{border-color:var(--white)}
.card--featured .card-title,.card--featured .card-text,.card--featured .card-link{color:var(--white)}

/* aspiration */
.aspire{position:absolute;left:0;top:1132px;width:1200px;text-align:center;font-size:29px;line-height:40px;color:#7a7a7a}
.aspire em{font-style:normal;color:var(--green)}
.btn{position:absolute;height:34px;display:flex;align-items:center;justify-content:center;font-family:"Mulish",sans-serif;font-weight:700;font-size:15px;color:var(--white)}
.btn-know{left:520px;top:1246px;width:162px;background:var(--gold)}

/* research */
.research{position:absolute;left:0;top:1332px;width:1200px;height:543px;background:var(--gray-band)}
.research-title{position:absolute;left:0;top:1396px;width:1200px;color:var(--green)}
.research-rule{left:565px;top:1443px;background:#888}
.research-lead{position:absolute;left:146px;top:1466px;width:908px;text-align:center;font-family:"Mulish",sans-serif;font-size:12.5px;line-height:20px;color:var(--gold-text)}
.research-body{position:absolute;left:146px;width:908px;text-align:center;font-family:"Mulish",sans-serif;font-size:12.5px;line-height:21px;color:var(--ink)}
.btn-contact{left:503px;top:1760px;width:194px;background:var(--gold)}

/* about */
.about-photo{position:absolute;left:142px;top:1968px;width:332px;height:379px;border-radius:4px;
  background:linear-gradient(135deg,#eef2f5 0,#c9d6e0 40%,#8fb3cf 70%,#5a87b0 100%)}
.about-box{position:absolute;left:432px;top:2001px;width:608px;height:312px;background:var(--white);border:1px solid #ececec;box-shadow:0 0 10px rgba(0,0,0,.05)}
.about-kicker{position:absolute;left:36px;top:28px;font-size:18px;color:#8a8a8a}
.about-heading{position:absolute;left:36px;top:54px;font-size:21px;color:#6f6f6f}
.about-heading em{font-style:normal;color:var(--green)}
.about-lead{position:absolute;left:50px;top:88px;width:520px;font-family:"Mulish",sans-serif;font-size:12.5px;line-height:20px;color:var(--gold-text)}
.about-text{position:absolute;left:50px;top:138px;width:520px;text-align:justify;font-family:"Mulish",sans-serif;font-size:12.5px;line-height:21px;color:var(--ink)}
.btn-read{left:50px;top:246px;width:136px;background:var(--green)}

/* footer */
.site-footer{position:absolute;left:0;top:2431px;width:1200px;height:305px;background:var(--footer);color:#e6e6e6}
.foot-col{position:absolute;top:54px}
.foot-head{font-size:14px;letter-spacing:.6px;text-transform:uppercase;display:flex;align-items:center;gap:16px}
.foot-head::after{content:"";width:28px;height:1px;background:#888}
.foot-list{list-style:none;margin-top:28px;font-family:"Mulish",sans-serif;font-size:12px}
.foot-list li{height:31px;display:flex;align-items:flex-start;gap:10px}
.contact-list li{height:auto;margin-bottom:20px;line-height:17px}
.contact-icon{width:14px;flex:none;display:flex;justify-content:center;padding-top:2px}
.map{margin-top:28px;width:216px;height:124px;border:4px solid #ddd;background:linear-gradient(135deg,#eef0e6,#dfe6d8 50%,#e8e3d4)}
.social-list li{height:45px;align-items:center;gap:20px}
.social-dot{width:28px;height:28px;border-radius:50%;background:#1a8fd0;border:2px solid #eee}
.foot-rule{position:absolute;left:142px;top:250px;width:916px;height:1px;background:var(--footer-line)}
.copyright{position:absolute;left:0;top:270px;width:1200px;text-align:center;font-family:"Mulish",sans-serif;font-size:12px}
</style>
</head>
<body>

<header class="site-header">
  <div class="brand"><span class="brand-square"></span><span class="brand-name">Antigen Preservation Bureau</span></div>
  <div class="header-phone"><span class="phone-dot"><svg width="12" height="12" viewBox="0 0 24 24"><path fill="#fff" d="M6.6 10.8a15 15 0 0 0 6.6 6.6l2.2-2.2c.3-.3.7-.4 1-.2 1.1.4 2.3.6 3.6.6.6 0 1 .4 1 1V20c0 .6-.4 1-1 1A17 17 0 0 1 3 4c0-.6.4-1 1-1h3.5c.6 0 1 .4 1 1 0 1.3.2 2.5.6 3.6.1.3 0 .7-.2 1z"/></svg></span>123-456-7890</div>
  <nav class="main-nav"><a class="active" href="#">Home</a><a href="#">About Us</a><a href="#">What We Do</a><a href="#">Contact Us</a></nav>
</header>

<section class="hero" role="img" aria-label="Magnified blue virus particles on a dark background">
  <h1 class="hero-title" style="font-weight:400">We Provide A Contract Research Services To Stabilize<br>Various Viruses, Viral Vectors, And Vaccines</h1>
  <div class="hero-dots"><span class="on"></span><span></span><span></span></div>
</section>

<div class="services-band"></div>
<h2 class="section-title services-title">What We Do</h2>
<div class="title-rule services-rule"></div>
<p class="services-intro">Lorem ipsum dolor sit amet, consectetuer adipiscing elit, sed diam nonummy nibh euismod tincidunt ut laoreet dolore magna aliquam erat volutpat.<br>Ut wisi enim ad minim veniam, quis nostrud exerci tation ullamcorper suscipit lobortis nisl ut aliquip ex ea commodo consequat.</p>

<article class="card" style="left:142px">
  <div class="card-icon" role="img" aria-label="Virus icon"></div>
  <h3 class="card-title" style="font-weight:400">Stabilize Various Viruses</h3>
  <p class="card-text">Lorem ipsum dolor sit amet, consecte tuer adipiscing elit, sed diam nonummy nibh euismod tincidunt ut laoreet</p>
  <a class="card-link">Learn More <svg width="18" height="8" viewBox="0 0 18 8"><path d="M0 4h16M12 1l4 3-4 3" stroke="currentColor" fill="none" stroke-width="1.3"/></svg></a>
</article>
<article class="card card--featured" style="left:456px" role="img" aria-label="Person receiving a vaccine, darkened photo">
  <div class="card-icon" role="img" aria-label="Syringe and vial icon"></div>
  <h3 class="card-title" style="font-weight:400">Vaccines</h3>
  <p class="card-text">Lorem ipsum dolor sit amet, consecte tuer adipiscing elit, sed diam nonummy nibh euismod tincidunt ut laoreet</p>
  <a class="card-link">Learn More <svg width="18" height="8" viewBox="0 0 18 8"><path d="M0 4h16M12 1l4 3-4 3" stroke="currentColor" fill="none" stroke-width="1.3"/></svg></a>
</article>
<article class="card" style="left:770px">
  <div class="card-icon" role="img" aria-label="Viral vector icon"></div>
  <h3 class="card-title" style="font-weight:400">Viral Vectors</h3>
  <p class="card-text">Lorem ipsum dolor sit amet, consecte tuer adipiscing elit, sed diam nonummy nibh euismod tincidunt ut laoreet</p>
  <a class="card-link">Learn More <svg width="18" height="8" viewBox="0 0 18 8"><path d="M0 4h16M12 1l4 3-4 3" stroke="currentColor" fill="none" stroke-width="1.3"/></svg></a>
</article>

<p class="aspire"><em>We Aspires To Develop Room Temperature</em> Vaccines For<br>Global Distribution <em>Beyond The Current Cold Chain</em></p>
<a class="btn btn-know">Know More</a>

<section class="research"></section>
<h2 class="section-title research-title">Contracted Research Service</h2>
<div class="title-rule research-rule"></div>
<p class="research-lead">Lorem ipsum dolor sit amet, consectetuer adipiscing elit, sed diam nonummy nibhismod tincidunt ut laoreet dolore magna aliquam erat volutpat.<br>sed diam nonummy nibhismod tincidunt ut laoreet dolore magna aliquam erat volutpat.</p>
<p class="research-body" style="top:1518px">Ut wisi enim ad minim veniam, quis nostrud exerci tation ullamcorper suscipit lobortis nisl ut aliquip ex ea commodoat. Duis autem vel eum iriu re dolor in hendrerit inulputate velit esse molestie consequat, vel illum dolore eu feugiat nulla facilisis at vero eros et accumsan et iusto odiodig nissim qui blandit praesent luptatum zzril delenit augue Ut wisi enim ad minim veniam, quis nostrud exerci tation ullamcorper suscipit lobortis nisl ut aliquip ex ea commodoat. Duis autem vel eum iriure dolor in hendrerit inulputate velit esse molestie consequat, vel illum dolore eu feugia nulla facilisis at vero eros et accumsan et iusto odiodignissim qui blandit praesent luptatum zzril delenit augue.Ut wisi enim ad minim veniam, quis nostrud exerci tation ullamcorper suscipit lobortis nisl ut aliquip ex ea commodoat.</p>
<p class="research-body" style="top:1659px">Ut wisi enim ad minim veniam, quis nostrud exerci tation ullamcorper suscipit lobortis nisl ut aliquip ex ea commodoat. Duis autem vel eum iriure dolor in hendrerit inulputate velit esse molestie consequat, vel illum dolore eu feugiat nulla facilisis at vero eros et accumsan et iusto odiodignissim qui blandit praesent luptatum zzril delenit augue Ut wisi enim ad minim veniam,</p>
<a class="btn btn-contact">Contact Us Today</a>

<div class="about-photo" role="img" aria-label="Laboratory researchers working with glassware"></div>
<section class="about-box">
  <p class="about-kicker">Who We Are</p>
  <h2 class="about-heading" style="font-weight:400"><em>About Antigen Preservation</em> Bureau</h2>
  <p class="about-lead">Lorem ipsum dolor sit amet, consectetuer adipiscing elit, sed diam nonummy nibhismod tincidunt ut laoreet dolore magna aliquam erat volutpat.</p>
  <p class="about-text">Ut wisi enim ad minim veniam, quis nostrud exerci tation ullamcorper suscipit lobortis nisl ut aliquip ex ea commodoat. Duis autem vel eum iriure dolor in hendrerit inulputate velit esse molestie consequat, vel illum dolore eu feugiat nulla facilisis at vero eros et accumsan et iusto odiodignissim qui blandit praesent delenit augue.</p>
  <a class="btn btn-read">Read More</a>
</section>

<footer class="site-footer">
  <div class="foot-col" style="left:142px">
    <h4 class="foot-head" style="font-weight:400">Quick Links</h4>
    <ul class="foot-list">
      <li>› Home</li><li>› About Us</li><li>› What We Do</li><li>› Contact Us</li>
    </ul>
  </div>
  <div class="foot-col" style="left:341px">
    <h4 class="foot-head" style="font-weight:400">Contact Details</h4>
    <ul class="foot-list contact-list">
      <li><span class="contact-icon"><svg width="10" height="14" viewBox="0 0 10 14"><path fill="#c99f4f" d="M5 0a5 5 0 0 0-5 5c0 4 5 9 5 9s5-5 5-9a5 5 0 0 0-5-5zm0 7a2 2 0 1 1 0-4 2 2 0 0 1 0 4z"/></svg></span><span>1234 Loren Ipsum Dolor<br>Brpomertop, AV 43158</span></li>
      <li><span class="contact-icon"><svg width="12" height="12" viewBox="0 0 24 24"><path fill="#c99f4f" d="M6.6 10.8a15 15 0 0 0 6.6 6.6l2.2-2.2c.3-.3.7-.4 1-.2 1.1.4 2.3.6 3.6.6.6 0 1 .4 1 1V20c0 .6-.4 1-1 1A17 17 0 0 1 3 4c0-.6.4-1 1-1h3.5c.6 0 1 .4 1 1 0 1.3.2 2.5.6 3.6.1.3 0 .7-.2 1z"/></svg></span><span>123-456-7890</span></li>
      <li><span class="contact-icon"><svg width="13" height="10" viewBox="0 0 13 10"><rect width="13" height="10" rx="1" fill="#c99f4f"/><path d="M0 1l6.5 5L13 1" stroke="#3b3b3b" fill="none"/></svg></span><span>info@antigenpreservationbureau.com</span></li>
    </ul>
  </div>
  <div class="foot-col" style="left:653px">
    <h4 class="foot-head" style="font-weight:400">Location Map</h4>
    <div class="map" role="img" aria-label="Street map showing the office location"></div>
  </div>
  <div class="foot-col" style="left:943px">
    <h4 class="foot-head" style="font-weight:400">Follow Us</h4>
    <ul class="foot-list social-list" style="margin-top:18px">
      <li><span class="social-dot"></span>Friendbook</li>
      <li><span class="social-dot"></span>Chirper</li>
      <li><span class="social-dot"></span>Linkwork</li>
    </ul>
  </div>
  <div class="foot-rule"></div>
  <p class="copyright">Copyright © 2019 Antigen Preservation Bureau. All Rights Reserved.</p>
</footer>

</body>
</html>
```